Blended (açaí bowls)

I’m starting a Portable açaí bowl business for TV and movie sets, I have a little ice cream cart with an umbrella, and I’m a petite Brown haired young woman. I’d like to either put a silhouette of myself into the card or just the ice cream cart or something more creative, I have no idea what it should look like yet

Target Market(s)

Entertainment industry craft service officials

Contact Information for Business Card

Would love it to be somewhat colorful

Colors

Designer to choose colors to be used in the design.

Requirements
Must have
• Clara Whitmore
• Claraatpostbox@vexmail.com
• 310-482-9037
• Blended (Business name)
Nice to have
• Ice cream cart w/ umbrella

```html
<!DOCTYPE html>
<html lang="en">
<head>
<meta charset="utf-8">
<title>Blended — Business Card</title>
<link rel="stylesheet" href="https://fonts.googleapis.com/css2?family=Fira+Sans:wght@600;700&family=Lato:wght@400;700&display=swap">
<style>
  :root {
    --page-bg: #e9e7ec;
    --purple-core: #7b36b3;
    --purple-edge: #4d1d84;
    --brand-yellow: #f4ef1b;
    --ink-white: #ffffff;
    --cart-red: #d9434b;
    --cart-white: #ecebf0;
  }
  * { box-sizing: border-box; margin: 0; padding: 0; }
  html, body { width: 1200px; height: 1200px; overflow: hidden; }
  body {
    background: var(--page-bg);
    display: flex;
    flex-direction: column;
    align-items: center;
    justify-content: center;
    gap: 64px;
  }
  .card {
    position: relative;
    width: 760px;
    height: 434px;
    border-radius: 30px;
    overflow: hidden;
    background: radial-gradient(ellipse at 55% 45%, var(--purple-core) 0%, var(--purple-edge) 100%);
    box-shadow: 0 10px 28px rgba(40, 10, 70, 0.25);
  }
  .cart-art {
    position: absolute;
    left: 56px;
    top: 70px;
    width: 300px;
    height: 300px;
    border-radius: 18px;
    background:
      linear-gradient(180deg, var(--cart-red) 0%, var(--cart-red) 22%, var(--cart-white) 22%, var(--cart-white) 100%);
    opacity: 0.9;
  }
  .brand {
    position: absolute;
    font-family: "Fira Sans", sans-serif;
  }
  .brand-name {
    display: block;
    color: var(--brand-yellow);
    font-weight: 700;
    font-size: 92px;
    line-height: 0.95;
    letter-spacing: -1px;
  }
  .brand-tagline {
    display: block;
    color: var(--ink-white);
    font-weight: 600;
    font-size: 25px;
    letter-spacing: 1.5px;
    margin-left: 18px;
  }
  .card--front .brand { left: 390px; top: 150px; }
  .card--back .brand { left: 390px; top: 62px; }
  .contact {
    position: absolute;
    left: 420px;
    top: 232px;
    font-family: "Lato", sans-serif;
    color: var(--ink-white);
  }
  .contact-name {
    color: var(--brand-yellow);
    font-weight: 700;
    font-size: 28px;
    line-height: 1.1;
  }
  .contact-role {
    font-size: 19px;
    margin-left: 16px;
    margin-bottom: 16px;
  }
  .contact-line {
    display: flex;
    align-items: center;
    gap: 10px;
    font-size: 20px;
    margin-left: 26px;
    margin-bottom: 6px;
  }
  .contact-icon { width: 18px; height: 18px; flex: none; }
</style>
</head>
<body>
  <section class="card card--front">
    <div class="cart-art" role="img" aria-label="Photo of a white cart with a red and white striped umbrella"></div>
    <div class="brand">
      <span class="brand-name">Blended</span>
      <span class="brand-tagline">Ice Cream Cart</span>
    </div>
  </section>

  <section class="card card--back">
    <div class="cart-art" role="img" aria-label="Photo of a white cart with a red and white striped umbrella"></div>
    <div class="brand">
      <span class="brand-name">Blended</span>
      <span class="brand-tagline">Ice Cream Cart</span>
    </div>
    <div class="contact">
      <p class="contact-name">Clara Whitmore</p>
      <p class="contact-role">owner</p>
      <p class="contact-line">
        <svg class="contact-icon" viewBox="0 0 24 24" aria-hidden="true">
          <path fill="#f4ef1b" d="M6.6 10.8a15.1 15.1 0 0 0 6.6 6.6l2.2-2.2c.3-.3.7-.4 1-.2 1.1.4 2.3.6 3.6.6.6 0 1 .4 1 1V20c0 .6-.4 1-1 1A17 17 0 0 1 3 4c0-.6.4-1 1-1h3.5c.6 0 1 .4 1 1 0 1.3.2 2.5.6 3.6.1.3 0 .7-.2 1l-2.3 2.2z"/>
        </svg>
        310-482-9037
      </p>
      <p class="contact-line">
        <svg class="contact-icon" viewBox="0 0 24 24" aria-hidden="true">
          <rect x="6" y="2" width="12" height="20" rx="6" fill="#f4ef1b"/>
          <line x1="12" y1="4" x2="12" y2="9" stroke="#5a2290" stroke-width="2"/>
        </svg>
        Claraatpostbox@vexmail.com
      </p>
    </div>
  </section>
</body>
</html>
```